Postcard Design for a book promotion

I have written a book which I want to market, and promo. The postcard is an advertisement for promotional purposes. The book is titled "Iron Orchard." By T.J. Havel. I have a website: http://ironorchard.info. I can upload graphics, photos or details.

The story is about a Waist Gunner and Crew 472 of the 517th Bomb Squadron who flew and fought over Germany in World War II.

All of the crew survived.

T J Havel, on Facebook and http://ironorchard. info

Promo

```html
<!DOCTYPE html>
<html lang="en">
<head>
<meta charset="utf-8">
<title>Iron Orchard – Promotional Postcard</title>
<link rel="stylesheet" href="https://fonts.googleapis.com/css2?family=Yellowtail&family=Arimo:ital,wght@0,400;0,700;1,400&family=Tinos:wght@400;700&display=swap">
<style>
  :root {
    --page: #e4e4e4;
    --ink: #0b0b0b;
    --panel: #111111;
    --sky-light: #a9a9a9;
    --sky-mid: #5c5c5c;
    --gold: #f2d64e;
    --cream: #f5ecc0;
    --white: #ffffff;
    --muted: #cfcfcf;
    --line: #9a9a9a;
    --paper: #ffffff;
  }
  * { box-sizing: border-box; margin: 0; padding: 0; }
  html, body { width: 857px; height: 1200px; overflow: hidden; }
  body { background: var(--page); font-family: "Arimo", Arial, sans-serif; position: relative; }

  .card { position: absolute; left: 28px; width: 800px; box-shadow: 0 4px 14px rgba(0,0,0,.35); overflow: hidden; }
  .card--front { top: 14px; height: 516px; background: var(--ink); }
  .card--back { top: 557px; height: 628px; background: var(--paper); }

  .hero-photo { position: absolute; inset: 0 0 150px 0;
    background: linear-gradient(180deg, var(--sky-light) 0%, #8c8c8c 45%, var(--sky-mid) 75%, var(--ink) 100%); }

  .tag-you { position: absolute; font-family: "Yellowtail", cursive; color: var(--cream); font-size: 46px; line-height: 1; }
  .tag-line { position: absolute; color: var(--gold); font-size: 21px; font-style: italic; }
  .tag-title { position: absolute; color: var(--gold); font-size: 40px; font-weight: 700; letter-spacing: 1px; }

  .author-photo { position: absolute; background: radial-gradient(circle at 45% 40%, #7a5b46, #3a2a22); }
  .author-photo--round { left: 45px; top: 340px; width: 122px; height: 122px; border-radius: 50%; border: 3px solid var(--white); }
  .author-photo--small { left: 40px; top: 395px; width: 92px; height: 108px; border: 2px solid var(--white); }

  .blurb { position: absolute; color: var(--white); font-size: 14px; line-height: 1.45; }
  .author-label { position: absolute; color: var(--white); font-size: 15px; }
  .author-name { position: absolute; color: var(--gold); font-size: 25px; font-weight: 700; letter-spacing: 1px; }
  .site { position: absolute; color: var(--white); font-size: 14px; font-family: "Tinos", serif; }

  .book { position: absolute; background: var(--white); box-shadow: 6px 8px 14px rgba(0,0,0,.55); text-align: center; font-family: "Tinos", serif; color: #111; }
  .book__title { font-weight: 400; }
  .book__art { margin: 0 auto; background: linear-gradient(180deg, #d8d8d8, #7d7d7d); }
  .book__blurb { color: #333; }
  .book--large { left: 568px; top: 176px; width: 182px; height: 272px; padding-top: 22px; }
  .book--large .book__title { font-size: 23px; }
  .book--large .book__art { width: 150px; height: 78px; margin-top: 16px; }
  .book--large .book__blurb { font-size: 8px; line-height: 1.3; padding: 12px 16px 0; }
  .book--large .book__author { font-size: 14px; margin-top: 40px; }
  .book--small { left: 168px; top: 382px; width: 108px; height: 158px; padding-top: 12px; }
  .book--small .book__title { font-size: 14px; }
  .book--small .book__art { width: 88px; height: 44px; margin-top: 9px; }
  .book--small .book__blurb { font-size: 5px; line-height: 1.3; padding: 7px 8px 0; }
  .book--small .book__author { font-size: 9px; margin-top: 20px; }

  .back-panel { position: absolute; left: 0; top: 0; width: 382px; height: 100%; background: var(--panel); }
  .stamp-box { position: absolute; left: 650px; top: 30px; width: 112px; height: 120px; border: 1.5px solid var(--line);
    color: #777; font-size: 13px; text-align: center; padding-top: 40px; line-height: 1.3; }
  .address-line { position: absolute; left: 432px; width: 330px; border-top: 1.5px solid var(--line); }
</style>
</head>
<body>

<section class="card card--front">
  <div class="hero-photo" role="img" aria-label="Black and white photograph of a WWII bomber aircraft in flight"></div>

  <div class="tag-you" style="left:38px; top:176px;">YOU</div>
  <div class="tag-line" style="left:40px; top:222px;">can't afford to Miss EITHER!</div>
  <div class="tag-title" style="left:38px; top:248px;">“IRON ORCHARD”</div>

  <div class="author-photo author-photo--round" role="img" aria-label="Portrait photo of the author seated"></div>

  <p class="blurb" style="left:198px; top:332px; width:340px;">The story is about a Waist Gunner and Crew 472 of the 517th Bomb Squadron who flew and fought over Germany in World War II.</p>
  <div class="author-label" style="left:198px; top:400px;">Author</div>
  <div class="author-name" style="left:198px; top:418px;">T.J. HAVEL</div>
  <div class="site" style="left:212px; top:462px;">http://ironorchard.info</div>

  <div class="book book--large">
    <div class="book__title">Iron Orchard</div>
    <div class="book__art" role="img" aria-label="Bomber aircraft image on the book cover"></div>
    <p class="book__blurb">The story of a waist gunner and his crew in the skies over Germany</p>
    <div class="book__author">T. J. Havel</div>
  </div>
</section>

<section class="card card--back">
  <div class="back-panel">
    <div class="tag-you" style="left:38px; top:24px;">YOU</div>
    <div class="tag-line" style="left:40px; top:70px;">can't afford to Miss EITHER!</div>
    <div class="tag-title" style="left:38px; top:96px; font-size:36px;">“IRON ORCHARD”</div>

    <p class="blurb" style="left:40px; top:168px; width:310px; font-size:14.5px;">This tribute is about the men who courageously flew and fought in peril, half frozen, suspended in the air five miles above the ground. The men of Crew 472 were more than ordinary men; they were extraordinary men doing an extraordinary job.</p>

    <div class="author-photo author-photo--small" role="img" aria-label="Portrait photo of the author seated"></div>
    <div class="author-label" style="left:66px; top:510px; font-size:12px;">Author</div>
    <div class="author-name" style="left:46px; top:526px; font-size:14px;">T.J. HAVEL</div>

    <div class="book book--small">
      <div class="book__title">Iron Orchard</div>
      <div class="book__art" role="img" aria-label="Bomber aircraft image on the book cover"></div>
      <p class="book__blurb">The story of a waist gunner and his crew in the skies over Germany</p>
      <div class="book__author">T. J. Havel</div>
    </div>
    <div class="site" style="left:164px; top:560px; font-size:12px;">http://ironorchard.info</div>
  </div>

  <div class="stamp-box">Place<br>Stamp<br>Here</div>
  <div class="address-line" style="top:420px;"></div>
  <div class="address-line" style="top:470px;"></div>
  <div class="address-line" style="top:520px;"></div>
  <div class="address-line" style="top:570px;"></div>
</section>

</body>
</html>
```